Interactive Theatre Infographic

The purpose in having this infographic is to educate our customers on how interactive theatre works.
Theatre attendees usually watch theatre and the characters never act as though they know there is an audience present.  This is known as the fourth wall.  With interactive theatre there is no fourth wall.  The audience is written into the narrative of the story.  The actors still perform scenes in a script but may require the audience to help solve problems, cast votes or on occasions audiences can find clues or make discoveries.  Each theatre event has a different design.  Within each show the audience will be taken to different locations(inside or outside) where scenes are enacted.  Actors may need to improvise their interactions with the audience.
From the audience perspective there are no lines to learn.  They do not have to get too involved.  The actors will control the interactions - the actors serve both as characters and guides.
There are three main components: the audience, the actors, and the story - all rolled into one.  A short synopis of interactive theatre works is below.
Interactive theatre – where you form part of the unfolding narrative.
Play witness to fully scripted performances in which actor led interaction means that you become involved in shaping the outcome of the story.  Where the fate of character lives may depend on the decisions you make.
Interactive theatre – where the fourth wall has been burned to the ground.  It’s just you, the characters and the story all rolled into one.
Book into a unique Brass Lantern Theatrical experience today – and maybe, just maybe, you might survive…..
Our website is www.brasslantern.com.au & an example of a theatre event can be seen at www.brasslantern.com.au/theatre/

Target Market(s)
Event customers. Theatre attendees. Age ranges wil be 18-50 most likely.
Requirements
Should not have
- Please do not use the image for our current theatre show. We need a generic design.

```html
<!DOCTYPE html>
<html lang="en">
<head>
<meta charset="utf-8">
<title>What Is Interactive Theatre?</title>
<link href="https://fonts.googleapis.com/css2?family=Bebas+Neue&family=Open+Sans:wght@400;600&display=swap" rel="stylesheet">
<style>
  :root {
    --ink: #121214;
    --red: #e8232b;
    --gold: #fdc010;
    --white: #ffffff;
    --stage: #4a4a4c;
    --rule: #6a6a6c;
  }
  * { margin: 0; padding: 0; box-sizing: border-box; }
  html, body { width: 849px; height: 1200px; overflow: hidden; background: var(--ink); }
  .infographic {
    position: relative; width: 849px; height: 1200px; background: var(--ink);
    color: var(--white); font-family: "Open Sans", Arial, sans-serif;
  }
  .abs { position: absolute; }
  .display { font-family: "Bebas Neue", Impact, sans-serif; font-weight: 400; letter-spacing: 0.5px; }
  .accent { color: var(--red); }
  .title { top: 30px; left: 0; width: 849px; text-align: center; font-size: 74px; line-height: 1; }
  .stage-art { border-radius: 4px; }
  .stage-left { left: 51px; top: 132px; width: 263px; height: 218px;
    background: linear-gradient(180deg, var(--stage) 0%, var(--stage) 62%, var(--gold) 62%, var(--gold) 78%, var(--ink) 78%); }
  .stage-right { left: 548px; top: 132px; width: 254px; height: 200px;
    background: linear-gradient(180deg, var(--stage) 0%, var(--stage) 68%, var(--gold) 68%, var(--gold) 88%, var(--ink) 88%); }
  .fourth-wall-line { left: 52px; top: 262px; }
  .intro { left: 326px; top: 146px; width: 200px; text-align: center; font-size: 12.3px; line-height: 15.6px; }
  .intro-lead { left: 316px; top: 255px; width: 220px; text-align: center; font-size: 12.3px; }
  .no-wall { left: 316px; top: 271px; width: 220px; text-align: center; font-size: 24px; color: var(--red); }
  .divider { left: 0; width: 849px; border-top: 1.5px dashed var(--rule); }
  .section-head { left: 0; width: 849px; text-align: center; font-size: 25px; line-height: 1; }
  .icon-row-caption { left: 0; width: 849px; top: 582px; text-align: center; font-size: 12.7px; font-weight: 600; }
  .crowd-art { background: var(--gold); border-radius: 10px 10px 14px 14px; }
  .people-art { background: var(--red); border-radius: 8px; }
  .locations-text { left: 414px; top: 679px; width: 310px; font-size: 12.7px; line-height: 17.5px; font-weight: 600; }
  .synopsis { left: 83px; top: 891px; width: 365px; font-size: 12.7px; line-height: 18.7px; text-align: justify; font-weight: 600; }
  .booking { left: 0; width: 849px; top: 1103px; text-align: center; font-size: 13.6px; font-weight: 600; }
  .site-url { left: 0; width: 849px; top: 1136px; text-align: center; font-size: 26px; color: var(--red); }
</style>
</head>
<body>
<main class="infographic">
  <h1 class="abs display title">What is <span class="accent">Interactive Theatre?</span></h1>

  <section class="fourth-wall">
    <div class="abs stage-art stage-left" role="img" aria-label="Traditional stage with curtains, two actors performing and a seated audience behind a dashed fourth wall"></div>
    <svg class="abs fourth-wall-line" width="270" height="30" viewBox="0 0 270 30" aria-hidden="true">
      <line x1="0" y1="6" x2="265" y2="28" stroke="#fff" stroke-width="2.5" stroke-dasharray="7 5"/>
    </svg>
    <p class="abs intro">In traditional theatre the characters never act as though they know there is an audience present. This is known as the fourth wall.</p>
    <p class="abs intro-lead">With interactive theatre there is</p>
    <p class="abs display no-wall">No fourth wall.</p>
    <div class="abs stage-art stage-right" role="img" aria-label="Stage with curtains where actors mingle with the audience and no fourth wall"></div>
  </section>

  <div class="abs divider" style="top:371px"></div>

  <section class="narrative">
    <h2 class="abs display section-head" style="top:390px">The audience is written <span class="accent">into the narrative of the story.</span></h2>

    <svg class="abs" style="left:93px;top:462px" width="116" height="86" viewBox="0 0 116 86" aria-label="Speech bubbles" role="img">
      <ellipse cx="32" cy="30" rx="32" ry="24" fill="var(--red)"/>
      <path d="M22 50 L18 66 L36 52 Z" fill="var(--red)"/>
      <text x="32" y="37" text-anchor="middle" font-family="Open Sans, sans-serif" font-weight="600" font-size="18" fill="#121214">?</text>
      <ellipse cx="90" cy="22" rx="24" ry="18" fill="var(--gold)"/>
      <path d="M96 36 L104 48 L84 38 Z" fill="var(--gold)"/>
      <text x="90" y="26" text-anchor="middle" font-size="14" font-weight="700" fill="#121214">···</text>
      <ellipse cx="84" cy="60" rx="22" ry="17" fill="var(--gold)"/>
      <path d="M88 74 L98 84 L78 76 Z" fill="var(--gold)"/>
      <text x="84" y="67" text-anchor="middle" font-family="Open Sans, sans-serif" font-weight="700" font-size="17" fill="#121214">!</text>
    </svg>

    <svg class="abs" style="left:242px;top:455px" width="68" height="88" viewBox="0 0 68 88" aria-label="Light bulb" role="img">
      <g stroke="var(--gold)" stroke-width="2.5" stroke-linecap="round">
        <line x1="34" y1="2" x2="34" y2="11"/><line x1="12" y1="8" x2="18" y2="15"/><line x1="56" y1="8" x2="50" y2="15"/>
        <line x1="3" y1="22" x2="11" y2="26"/><line x1="65" y1="22" x2="57" y2="26"/>
      </g>
      <path d="M34 24 a19 19 0 0 1 12 34 v8 h-24 v-8 a19 19 0 0 1 12 -34 z" fill="none" stroke="var(--red)" stroke-width="5"/>
      <rect x="22" y="68" width="24" height="5" rx="2" fill="var(--red)"/>
      <rect x="24" y="75" width="20" height="5" rx="2" fill="var(--red)"/>
      <rect x="28" y="82" width="12" height="4" rx="2" fill="var(--red)"/>
    </svg>

    <div class="abs crowd-art" style="left:349px;top:476px;width:126px;height:68px" role="img" aria-label="Cheering audience crowd silhouette"></div>

    <svg class="abs" style="left:497px;top:478px" width="78" height="68" viewBox="0 0 78 68" aria-label="Magnifying glass" role="img">
      <circle cx="22" cy="22" r="17" fill="none" stroke="var(--red)" stroke-width="5"/>
      <path d="M34 34 L74 64 L70 66 L32 38 Z" fill="var(--red)"/>
    </svg>

    <svg class="abs" style="left:603px;top:478px" width="160" height="70" viewBox="0 0 160 70" aria-label="Dashed trail ending at an X" role="img">
      <path d="M6 62 C0 40, 40 44, 28 30 C18 18, 20 4, 40 4 C62 4, 70 20, 74 36 C78 56, 100 68, 116 50" fill="none" stroke="var(--gold)" stroke-width="2.5" stroke-dasharray="5 5"/>
      <g stroke="var(--red)" stroke-width="6" stroke-linecap="round">
        <line x1="124" y1="24" x2="150" y2="46"/><line x1="150" y1="24" x2="124" y2="46"/>
      </g>
    </svg>

    <p class="abs icon-row-caption">The actors may require the audience to solve problems, cast votes, find clues or make discoveries</p>

    <svg class="abs" style="left:161px;top:658px" width="220" height="78" viewBox="0 0 220 78" aria-label="Map pins joined by a dashed route" role="img">
      <path d="M12 75 L60 64 L120 78 L190 64" fill="none" stroke="#fff" stroke-width="2.5" stroke-dasharray="6 5"/>
      <path d="M60 64 L68 44 L110 34" fill="none" stroke="#fff" stroke-width="2.5" stroke-dasharray="6 5"/>
      <path d="M16 22 a13 13 0 0 1 26 0 c0 12 -13 24 -13 44 c0 -20 -13 -32 -13 -44 z" fill="var(--red)"/>
      <circle cx="29" cy="22" r="5" fill="#121214"/>
      <path d="M109 8 a9 9 0 0 1 18 0 c0 9 -9 16 -9 30 c0 -14 -9 -21 -9 -30 z" fill="var(--red)"/>
      <circle cx="118" cy="8" r="3.5" fill="#121214"/>
      <path d="M197 36 a8 8 0 0 1 16 0 c0 8 -8 14 -8 26 c0 -12 -8 -18 -8 -26 z" fill="var(--gold)"/>
      <circle cx="205" cy="36" r="3" fill="#121214"/>
    </svg>
    <p class="abs locations-text">Within each show the audience will be taken to different locations(inside or outside) where scenes are enacted.</p>
  </section>

  <div class="abs divider" style="top:777px"></div>

  <section class="synopsis-block">
    <h2 class="abs display section-head" style="top:804px">Interactive Theatre – <span class="accent">where you form part of the unfolding narrative.</span></h2>
    <p class="abs synopsis">Play witness to fully scripted performances in which actor led interaction means that you become involved in shaping the outcome of the story. Where the fate of character lives may depend on the decisions you make. Where the fourth wall has been burned to the ground. It’s just you, the characters and the story all rolled into one.</p>

    <svg class="abs" style="left:550px;top:852px" width="180" height="180" viewBox="0 0 180 180" aria-hidden="true">
      <circle cx="90" cy="90" r="85" fill="none" stroke="var(--rule)" stroke-width="1.5" stroke-dasharray="6 5"/>
    </svg>
    <div class="abs crowd-art" style="left:535px;top:882px;width:92px;height:48px" role="img" aria-label="Audience crowd silhouette"></div>
    <svg class="abs" style="left:666px;top:880px" width="100" height="72" viewBox="0 0 100 72" aria-label="Open book" role="img">
      <path d="M4 30 L50 50 L96 22 L96 30 L50 60 L4 40 Z" fill="#fff"/>
      <path d="M8 26 L48 44 L48 10 C36 4, 22 6, 8 14 Z" fill="#121214" stroke="#fff" stroke-width="3"/>
      <path d="M52 44 L92 20 L86 2 C74 4, 62 6, 52 10 Z" fill="#121214" stroke="#fff" stroke-width="3"/>
      <g stroke="#fff" stroke-width="2"><line x1="16" y1="22" x2="42" y2="32"/><line x1="16" y1="28" x2="42" y2="38"/><line x1="58" y1="18" x2="82" y2="10"/><line x1="58" y1="26" x2="84" y2="16"/></g>
    </svg>
    <div class="abs people-art" style="left:590px;top:958px;width:96px;height:68px" role="img" aria-label="Three actors performing a scene"></div>
  </section>

  <h2 class="abs display section-head" style="top:1058px">The audience, the actors, and the story – <span class="accent">all rolled into one.</span></h2>
  <p class="abs booking">Book into a unique Brass Lantern Theatrical experience today – and maybe, just maybe, you might survive.....</p>
  <p class="abs display site-url">www.brasslantern.com.au/theatre/</p>
</main>
</body>
</html>
```